FREE SOCIAL SECURITY DISABILITY CLAIM EVALUATION - Ad Banners & Email Marketing Creatives

Looking for design of ad banners and email creative for my Social Security Disability Insurance Benefits Application, Denial, & Appeals Help website. Call to action based email focused on conveying brand, messaging of "Are you out of work due to a disability? You may qualify for up to $2,642 per month in Social Security Disability benefits!" and "ACT NOW: Check Your Eligibility" Call to action of 'Get Your FREE Evaluation' or 'Fast, FREE, No Obligation Evaluation' or 'Confirm My Eligibility Now!' or 'Start My FREE Evaluation' or 'Confirm My Eligibility Now!'. Can use any messaging and images from the current website:
https://benefitharborline.com/

Please focus on imaging that matches the site. The final Ad Banners must be delivered in both JPG and PSD file formats. Ad Banners must follow RQO standards.

We need Ad Banners in the following sizes.
728x90
300x250
336x280
160x600
1200x628
600x600
1080x1080
Email

Target Market(s)
People in the US between the ages 48-63 looking for Social Security Disability Insurance Benefits Application, Denial, & Appeals Help. Get connected to a local Social Security Disability legal representative for a free, no-obligation evaluation. Find out if you are eligible to receive financial compensation for as much as $2,642 a month!

Should not be cookie cutter. Stick to simple yet official looking.

The final Email creative must be done in responsive HTML as well as text for easy use and include Email Opt Out link etc.

Target Market(s)

Americans that are between the ages 48-63 that have a physical condition that prevents them from working. Many times the physical condition is a result of an injury.

Coding

Coded - Design and coding required

Font styles to use
Sans Serif

Requirements
Must have
• A strong call to action.
Should not have
• No photos of people in wheelchairs.

```html
<!DOCTYPE html>
<html lang="en">
<head>
<meta charset="utf-8">
<title>Disability Evaluation Ad Banners</title>
<link href="https://fonts.googleapis.com/css2?family=Poppins:wght@400;500;600;700&display=swap" rel="stylesheet">
<style>
  :root {
    --page: #ffffff;
    --black: #000000;
    --white: #ffffff;
    --orange: #fd8a0a;
    --orange-deep: #f57f00;
    --cta: #1aa7ec;
    --photo-grey: #8a929b;
    --photo-warm: #5a4038;
    --photo-maroon: #4a2a2c;
  }
  * { box-sizing: border-box; margin: 0; padding: 0; }
  html, body { width: 1200px; height: 469px; overflow: hidden; background: var(--page); }
  body { position: relative; font-family: "Poppins", sans-serif; color: var(--white); }

  .banner { position: absolute; overflow: hidden; box-shadow: 0 2px 6px rgba(0,0,0,.18); }
  .size-tag { position: absolute; font-size: 7px; font-weight: 500; letter-spacing: .3px; }
  .cta {
    position: absolute; display: flex; align-items: center; justify-content: center;
    background: var(--cta); color: var(--white); font-weight: 400; white-space: nowrap;
    border-radius: 1px;
  }
  .headline { position: absolute; font-weight: 700; line-height: 1; }
  .copy { position: absolute; line-height: 1.55; }

  /* Landscape 1200x628 */
  .banner--landscape { left: 21px; top: 22px; width: 473px; height: 247px; background: var(--black); }
  .banner--landscape .photo {
    position: absolute; left: 0; top: 0; width: 220px; height: 100%;
    background: linear-gradient(90deg, var(--photo-grey) 0%, #7b828a 55%, rgba(0,0,0,0) 100%);
  }
  .banner--landscape .headline { left: 191px; top: 48px; font-size: 19px; line-height: 28px; letter-spacing: .4px; }
  .banner--landscape .offer { left: 191px; top: 104px; font-size: 10.5px; line-height: 15.5px; }
  .banner--landscape .promise { left: 191px; top: 137px; font-size: 10.5px; line-height: 15.5px; }
  .banner--landscape .cta { left: 191px; top: 174px; width: 136px; height: 20px; font-size: 7.6px; }
  .banner--landscape .size-tag { right: 12px; bottom: 10px; }

  /* Square 600x600 */
  .banner--square { left: 505px; top: 22px; width: 237px; height: 236px; background: var(--photo-warm); }
  .banner--square .photo {
    position: absolute; inset: 0;
    background: radial-gradient(circle at 60% 45%, #7a5a4e 0%, #4d3a36 55%, #33292a 100%);
  }
  .banner--square .content { position: absolute; left: 0; top: 0; width: 100%; text-align: center; }
  .banner--square .headline { position: static; margin-top: 38px; font-size: 12px; line-height: 17.5px; letter-spacing: .3px; }
  .banner--square .offer { position: static; margin-top: 4px; font-size: 8px; line-height: 15.5px; }
  .banner--square .promise { position: static; margin-top: 1px; font-size: 8px; font-weight: 700; line-height: 13.5px; }
  .banner--square .cta { left: 62px; top: 139px; width: 112px; height: 19px; font-size: 7px; }
  .banner--square .waves { position: absolute; left: 0; top: 0; }
  .banner--square .size-tag { right: 11px; top: 8px; }

  /* Social 1080x1080 */
  .banner--social { left: 754px; top: 22px; width: 426px; height: 426px; background: var(--photo-maroon); }
  .banner--social .photo {
    position: absolute; inset: 0;
    background: linear-gradient(135deg, #8a7a72 0%, #6b4a44 35%, #4a2a2c 70%, #3a2326 100%);
  }
  .banner--social .arc { position: absolute; left: 0; top: 0; }
  .banner--social .headline { left: 178px; font-size: 23px; letter-spacing: .6px; }
  .banner--social .line-1 { top: 101px; }
  .banner--social .line-2 { top: 141px; }
  .banner--social .line-3 { top: 170px; font-size: 39px; letter-spacing: .5px; }
  .banner--social .offer { left: 178px; top: 220px; font-size: 10.5px; line-height: 18px; }
  .banner--social .promise { left: 177px; top: 259px; font-size: 10.3px; font-weight: 700; line-height: 18px; letter-spacing: .2px; }
  .banner--social .cta { left: 178px; top: 297px; width: 166px; height: 26px; font-size: 10.5px; }
  .banner--social .size-tag { right: 14px; bottom: 9px; }
</style>
</head>
<body>

<section class="banner banner--landscape">
  <div class="photo" role="img" aria-label="Photo of a smiling senior woman with glasses resting her hands on a walking cane"></div>
  <h1 class="headline">Unable to Work<br>Due to a Disability?</h1>
  <p class="copy offer">You may qualify for up to $2,642 per month<br>in Social Security Disability Benefits</p>
  <p class="copy promise">Fast, Free &amp; No Obligation Evaluation<br>&nbsp;- Only Takes 30-Seconds!</p>
  <a class="cta">CHECK MY ELIGIBILITY NOW</a>
  <span class="size-tag">1200X628</span>
</section>

<section class="banner banner--square">
  <div class="photo" role="img" aria-label="Photo of a senior couple embracing warmly"></div>
  <svg class="waves" width="237" height="236" viewBox="0 0 237 236" aria-hidden="true">
    <path fill="var(--orange)" d="M0,128 C35,132 52,155 56,180 C85,190 108,210 122,236 C130,215 145,205 160,207 C175,207 185,215 188,222 C200,200 220,188 237,186 L237,236 L0,236 Z"/>
    <g fill="none" stroke="var(--white)" stroke-width="2.6" stroke-linecap="round" stroke-linejoin="round">
      <circle cx="51" cy="206" r="2.6" fill="var(--white)" stroke="none"/>
      <path d="M51,211 L51,222 L61,222 L65,231"/>
      <path d="M45,216 A10,10 0 1 0 60,230"/>
      <path d="M25,183 q-4,8 3,10 q8,2 9,-8 q-2,-6 -8,-6"/>
      <path d="M33,196 q3,8 10,5 q6,-3 3,-10 q-4,-4 -9,-1"/>
      <circle cx="156" cy="215" r="2.2" fill="var(--white)" stroke="none"/>
      <path d="M155,219 L153,231 M155,222 L160,226 M153,231 L150,238 M154,231 L157,238 M161,225 L161,238"/>
      <path d="M213,228 q-4,-12 6,-17 q10,-3 14,6 q2,7 -3,11 l0,5"/>
      <path d="M218,220 q4,-4 8,0"/>
    </g>
  </svg>
  <div class="content">
    <h2 class="headline">Unable to Work<br>Due to a Disability?</h2>
    <p class="copy offer">You may qualify for up to $2,642 per month<br>in Social Security Disability Benefits</p>
    <p class="copy promise">Fast, Free &amp; No Obligation Evaluation<br>- Only Takes 30-Seconds!</p>
  </div>
  <a class="cta">CHECK MY ELIGIBILITY NOW</a>
  <span class="size-tag">600X600</span>
</section>

<section class="banner banner--social">
  <div class="photo" role="img" aria-label="Photo of a smiling senior couple hugging cheek to cheek"></div>
  <svg class="arc" width="426" height="426" viewBox="0 0 426 426" aria-hidden="true">
    <circle cx="394" cy="220" r="264" fill="var(--orange)" opacity=".96"/>
  </svg>
  <h2 class="headline line-1">Unable to</h2>
  <h2 class="headline line-2">Work Due to a</h2>
  <h2 class="headline line-3">Disability?</h2>
  <p class="copy offer">You may qualify for up to $2,642 per month<br>in Social Security Disability Benefits</p>
  <p class="copy promise">Fast, Free &amp; No Obligation Evaluation<br>- Only Takes 30-Seconds!</p>
  <a class="cta">CHECK MY ELIGIBILITY NOW</a>
  <span class="size-tag">1080X1080</span>
</section>

</body>
</html>
```